Dental Office Business Card

We need a business card for our pediatric dentistry office.
On one side the design needs to contain the following:
our logo (attached)
Vento Pediatric Grins
Soraya Kadbelani, DDS
Board Certified Pediatric Dentist
Tel: (555) 318-2747)
Fax: (555) 264-8031
Email: info@ventopediatricgrins.example
Web: www.ventopediatricgrins.example
Address: 41 Brindle Ave, Suite 208, Ashbury Glen, AG 02099

On the other side of the card, the design needs to have an appointment reminder (date and time as well as day of the week) similar to the design attached (no need for appointment reason “For”)

```html
<!DOCTYPE html>
<html lang="en">
<head>
<meta charset="utf-8">
<title>Vento Pediatric Grins – Business Card</title>
<link rel="stylesheet" href="https://fonts.googleapis.com/css2?family=Lato:wght@300;400;700;900&display=swap">
<style>
  :root {
    --backdrop: #8f8f8f;
    --card: #ffffff;
    --ink: #222222;
    --mint: #a5d9aa;
    --text: #333333;
    --leader: #555555;
  }
  html, body {
    margin: 0;
    padding: 0;
    width: 1200px;
    height: 1200px;
    overflow: hidden;
    background: var(--backdrop);
    font-family: "Lato", sans-serif;
    color: var(--ink);
  }
  .card {
    position: absolute;
    left: 250px;
    width: 700px;
    height: 400px;
    background: var(--card);
    border-radius: 20px;
    box-shadow: 0 2px 6px rgba(0,0,0,0.25);
    overflow: hidden;
  }
  .card--front { top: 170px; }
  .card--back { top: 631px; }

  /* Front */
  .accent-bar {
    position: absolute;
    left: 0; top: 37px;
    width: 15px; height: 38px;
    background: var(--mint);
  }
  .dentist-name {
    position: absolute;
    left: 37px; top: 30px;
    margin: 0;
    font-size: 23px;
    font-weight: 900;
    letter-spacing: 0.2px;
    white-space: nowrap;
  }
  .dentist-title {
    position: absolute;
    left: 37px; top: 59px;
    margin: 0;
    font-size: 16px;
    font-weight: 400;
    color: var(--mint);
    letter-spacing: 0.3px;
  }
  .contact-list {
    position: absolute;
    left: 37px; top: 98px;
    margin: 0; padding: 0;
    list-style: none;
    font-size: 16px;
    color: var(--text);
    letter-spacing: 0.4px;
  }
  .contact-item {
    display: flex;
    align-items: flex-start;
    line-height: 24px;
    white-space: nowrap;
  }
  .contact-item--address { margin-bottom: 6px; }
  .contact-icon {
    width: 14px; height: 14px;
    margin: 5px 12px 0 0;
    flex: none;
    fill: var(--mint);
  }
  .brand {
    position: absolute;
    left: 37px; top: 270px;
    color: var(--ink);
    font-weight: 900;
    line-height: 1;
  }
  .brand-name { display: block; font-size: 80px; letter-spacing: -1px; }
  .brand-tag { display: block; font-size: 21px; margin-top: -2px; letter-spacing: 0.4px; }
  .brand-decoration {
    position: absolute;
    left: 345px; top: 55px;
    width: 290px; height: 290px;
    border-radius: 50%;
    background: var(--mint);
  }

  /* Back */
  .reminder-brand {
    position: absolute;
    top: 76px; left: 0; right: 0;
    display: flex;
    flex-direction: column;
    align-items: center;
    font-weight: 900;
    color: var(--ink);
    line-height: 1;
  }
  .reminder-brand-row { display: flex; align-items: center; gap: 14px; }
  .reminder-brand-mark {
    width: 44px; height: 44px;
    border-radius: 50%;
    background: var(--mint);
  }
  .reminder-brand-name { font-size: 58px; letter-spacing: -1px; }
  .reminder-brand-tag { font-size: 25px; margin-top: 6px; letter-spacing: 0.4px; }

  .form-row {
    position: absolute;
    left: 52px; right: 58px;
    display: flex;
    align-items: baseline;
    font-size: 16px;
    color: var(--ink);
  }
  .form-row--name { top: 200px; }
  .form-row--when { top: 258px; }
  .form-field { flex: 1; border-bottom: 1px dotted var(--leader); margin: 0 1px; height: 14px; }
  .form-field--date { flex: 0 0 248px; }
  .form-suffix { font-size: 13px; margin-left: 1px; }

  .day-list {
    position: absolute;
    top: 320px; left: 113px;
    margin: 0; padding: 0;
    list-style: none;
    display: flex;
    font-size: 17px;
  }
  .day { display: flex; align-items: center; }
  .day-box {
    width: 13px; height: 13px;
    border: 2px solid var(--mint);
    margin-right: 9px;
  }
  .day--mon { width: 90px; }
  .day--tue { width: 88px; }
  .day--wed { width: 86px; }
  .day--thu { width: 82px; }
  .day--fri { width: 73px; }
</style>
</head>
<body>

<section class="card card--front" aria-label="Business card front">
  <span class="accent-bar"></span>
  <h1 class="dentist-name">SORAYA KADBELANI, DDS</h1>
  <p class="dentist-title">Board Certified Pediatric Dentist</p>

  <ul class="contact-list">
    <li class="contact-item contact-item--address">
      <svg class="contact-icon" viewBox="0 0 14 14"><path d="M7 0a5 5 0 0 0-5 5c0 3.6 5 9 5 9s5-5.4 5-9a5 5 0 0 0-5-5zm0 7a2 2 0 1 1 0-4 2 2 0 0 1 0 4z"/></svg>
      <span>41 Brindle Ave, Suite 208<br>Ashbury Glen, AG 02099</span>
    </li>
    <li class="contact-item">
      <svg class="contact-icon" viewBox="0 0 14 14"><path d="M3 1l2.2 2.6-1.2 1.6c.8 1.8 2.2 3.2 4 4l1.6-1.2L12.2 10.3 10.8 13C5.5 12.4 1.6 8.5 1 3.2z"/></svg>
      <span>(555) 318-2747)</span>
    </li>
    <li class="contact-item">
      <svg class="contact-icon" viewBox="0 0 14 14"><path d="M3 1h8v3H3zM1 5h12v6h-2V9H3v2H1zM4 10h6v4H4z"/></svg>
      <span>(555) 264-8031</span>
    </li>
    <li class="contact-item">
      <svg class="contact-icon" viewBox="0 0 14 14"><path d="M1 3h12v8H1zm1 1.2V5l5 3 5-3v-.8L7 7.2z"/></svg>
      <span>info@ventopediatricgrins.example</span>
    </li>
    <li class="contact-item">
      <svg class="contact-icon" viewBox="0 0 14 14"><path d="M7 0a7 7 0 1 0 0 14A7 7 0 0 0 7 0zm0 1.5a5.5 5.5 0 0 1 4.4 8.8L9 8l-2-.5L5 9l-1 3A5.5 5.5 0 0 1 2 4l3 1 1.5-2z"/></svg>
      <span>ventopediatricgrins.example</span>
    </li>
  </ul>

  <div class="brand">
    <span class="brand-name">Vento</span>
    <span class="brand-tag">PEDIATRIC GRINS</span>
  </div>

  <div class="brand-decoration" role="img" aria-label="Large brand symbol decoration area"></div>
</section>

<section class="card card--back" aria-label="Appointment reminder card back">
  <div class="reminder-brand">
    <div class="reminder-brand-row">
      <span class="reminder-brand-mark"></span>
      <span class="reminder-brand-name">Vento</span>
    </div>
    <span class="reminder-brand-tag">PEDIATRIC GRINS</span>
  </div>

  <div class="form-row form-row--name">
    <span>NAME</span><span class="form-field"></span>
  </div>
  <div class="form-row form-row--when">
    <span>DATE</span><span class="form-field form-field--date"></span>
    <span>TIME</span><span class="form-field"></span>
    <span class="form-suffix">AM\PM</span>
  </div>

  <ul class="day-list">
    <li class="day day--mon"><span class="day-box"></span>MON</li>
    <li class="day day--tue"><span class="day-box"></span>TUES</li>
    <li class="day day--wed"><span class="day-box"></span>WED</li>
    <li class="day day--thu"><span class="day-box"></span>THU</li>
    <li class="day day--fri"><span class="day-box"></span>FRI</li>
    <li class="day"><span class="day-box"></span>SAT</li>
  </ul>
</section>

</body>
</html>
```